Stationary/business card/envelope design for Hollowmere Dentalcare

We are located in the foothills of the sierra nevada mountains. We are looking for a beautiful classy modern stationary. We need evelopes and business card design all to flow seamlessly. Envelope design.

Additional office address 8614 Westgate Ct., Suite B, Auburn, CA 95847 Phone: pending Fax: pending.

3 different Drs on each business card:
Marla J. Osgood, DDS
Tova R. Osgood, DDS
Rebecca M. Halvorsen, DDS

Target Market(s)

Dental patients

Industry/Entity Type

Dental

Contact Information for Business Card

Two sided. See example.

Font styles to use
Sans Serif

Requirements
Must have
• One sided business cards. Need envelope design.
Colors should match existing logo.

Marla J. Osgood, DDS
Tova R. Osgood, DDS
Rebecca M. Halvorsen, DDS

```html
<!DOCTYPE html>
<html lang="en">
<head>
<meta charset="utf-8">
<title>Hollowmere Dentalcare — Stationery Set</title>
<link href="https://fonts.googleapis.com/css2?family=Tinos&family=Great+Vibes&family=Montserrat:wght@400;500;600&display=swap" rel="stylesheet">
<style>
:root{
  --green:#2a7d3f;
  --blue:#2fb3dc;
  --ink:#222;
  --muted:#999;
  --paper:#fff;
  --backdrop:#d9dadc;
  --line:#9aa;
}
*{box-sizing:border-box;margin:0;padding:0}
html,body{width:1200px;height:1200px;overflow:hidden;background:var(--backdrop)}
body{position:relative;font-family:"Tinos",serif;color:var(--ink)}
.sheet{position:absolute;background:var(--paper);overflow:hidden}
.wave{position:absolute;left:0;width:100%}
.brand{display:flex;align-items:center;gap:6px;color:var(--green);font-family:"Tinos",serif;position:absolute}
.brand .dot{border-radius:50%;background:var(--blue);flex:none}

/* business card */
.business-card{left:72px;top:88px;width:510px;height:290px}
.business-card .brand{left:60px;top:125px;font-size:21px;line-height:1.1;width:150px}
.business-card .brand .dot{width:34px;height:34px}
.business-card .divider{position:absolute;left:255px;top:60px;width:1px;height:172px;background:#555}
.business-card .details{position:absolute;left:275px;top:56px;font-size:13.5px;line-height:17px}
.doctor{font-family:"Great Vibes",cursive;color:var(--green);font-size:24px;line-height:28px}
.details .gap{height:11px}
.label{color:var(--green)}

/* appointment card */
.appointment-card{left:618px;top:90px;width:511px;height:291px}
.appointment-card h2{position:absolute;top:32px;width:100%;text-align:center;font-weight:400;font-size:24px;color:var(--green);letter-spacing:.3px}
.appointment-card .dash{position:absolute;left:34px;right:32px;top:129px;border-top:1px dashed var(--line)}
.appointment-card .row{position:absolute;left:36px;right:30px;font-size:14.5px;display:flex;justify-content:space-between}
.box{display:inline-block;width:11px;height:11px;border:2px solid var(--green);margin-right:7px;vertical-align:-1px}
.appointment-card .rule{position:absolute;left:0;right:0;top:256px;height:2px;background:var(--green)}
.appointment-card .band{position:absolute;left:0;right:0;top:261px;bottom:0;background:var(--blue);color:#fff;text-align:center;font-size:15px;line-height:30px}

/* letterhead */
.letterhead{left:72px;top:418px;width:486px;height:689px;font-family:"Montserrat",sans-serif}
.letterhead .brand{left:40px;top:50px;font-size:10px;width:75px;line-height:1.15}
.letterhead .brand .dot{width:16px;height:16px}
.letterhead .to{position:absolute;left:49px;top:154px;font-size:8px;letter-spacing:1px}
.letterhead .date{position:absolute;right:49px;top:154px;font-size:6.5px;color:#666}
.recipient{position:absolute;left:49px;top:168px;font-size:6px;line-height:10.5px;color:var(--muted)}
.recipient strong{color:var(--green);font-size:7.5px;font-weight:600}
.body-text{position:absolute;left:49px;width:389px;top:246px;font-size:6.4px;line-height:8.6px;color:#8a8a8a;text-align:justify}
.body-text p{margin-bottom:8px}
.signature{position:absolute;left:50px;top:585px}
.signature .script{font-family:"Great Vibes",cursive;font-size:18px;color:#333}
.signature .name{font-size:7.5px;font-weight:500;margin-top:4px}
.signature .role{font-size:6px;color:var(--muted)}
.letterhead .footer{position:absolute;left:46px;right:46px;top:658px;font-family:"Tinos",serif;font-size:7.2px;text-align:center;line-height:10.5px}
.footer .addr{display:flex;align-items:center;gap:4px}
.footer .addr::before,.footer .addr::after{content:"";flex:1;border-top:1px solid #777}

/* envelope front */
.envelope-front{left:575px;top:485px;width:548px;height:237px}
.envelope-front .brand{left:18px;top:35px;font-size:11px;width:90px;line-height:1.15}
.envelope-front .brand .dot{width:18px;height:18px}
.return-address{position:absolute;left:17px;top:94px;font-size:7.5px;line-height:10px}

/* envelope back */
.envelope-back{left:575px;top:801px;width:551px;height:239px}
.envelope-back .brand{left:238px;top:14px;font-size:7.5px;width:80px;line-height:1.15}
.envelope-back .brand .dot{width:12px;height:12px}
.envelope-back .site{position:absolute;bottom:11px;width:100%;text-align:center;font-size:8.5px}
</style>
</head>
<body>

<section class="sheet business-card">
  <div class="brand"><span class="dot"></span><span>Hollowmere Dentalcare</span></div>
  <div class="divider"></div>
  <div class="details">
    <div class="doctor">Marla J. Osgood, DDS</div>
    <div>Family &amp; Cosmetic Dentistry</div>
    <div class="gap"></div>
    <div>5120 Ridgecrest Road</div>
    <div>Granite Bay, California 95790</div>
    <div class="gap"></div>
    <div><span class="label">Office:</span> (530) 555-0142</div>
    <div><span class="label">Fax:</span> (530) 555-0187</div>
    <div>hollowmeredentalcare@mail.com</div>
    <div>www.hollowmeredentalcare.com</div>
  </div>
  <svg class="wave" style="top:0;height:290px" viewBox="0 0 510 290" preserveAspectRatio="none">
    <path d="M0 263 C150 250 330 292 510 260 L510 290 L0 290Z" fill="var(--blue)"/>
    <path d="M0 250 C70 238 150 246 175 256 C120 251 50 254 0 262Z" fill="var(--green)"/>
    <path d="M340 278 C420 276 480 264 510 250 L510 257 C470 272 410 281 340 278Z" fill="var(--green)"/>
  </svg>
</section>

<section class="sheet appointment-card">
  <h2>HAS AN APPOINTMENT ON</h2>
  <div class="dash"></div>
  <div class="row" style="top:184px">
    <span><span class="box"></span>MON</span><span><span class="box"></span>TUE</span><span><span class="box"></span>WED</span><span><span class="box"></span>THU</span><span><span class="box"></span>FRI</span><span><span class="box"></span>SAT</span>
  </div>
  <div class="row" style="top:210px;left:54px;right:62px">
    <span>DATE ______________</span><span>TIME _________</span><span><span class="box"></span>AM</span><span><span class="box"></span>PM</span>
  </div>
  <div class="rule"></div>
  <div class="band">www.hollowmeredentalcare.com</div>
</section>

<section class="sheet letterhead">
  <svg class="wave" style="top:0;height:56px" viewBox="0 0 486 56" preserveAspectRatio="none">
    <path d="M0 0 L486 0 L486 36 C380 20 200 20 0 22Z" fill="var(--blue)"/>
    <path d="M0 34 C40 20 110 16 160 18 C100 22 40 30 0 40Z" fill="var(--green)"/>
    <path d="M300 28 C380 28 440 36 486 40 L486 46 C430 42 370 32 300 28Z" fill="var(--green)"/>
  </svg>
  <div class="brand"><span class="dot"></span><span>Hollowmere Dentalcare</span></div>
  <div class="to">TO</div>
  <div class="date">Friday, 01/01/2018</div>
  <div class="recipient">
    <strong>Evan Ridley</strong><br>Human Resources<br>Northfield Inc.<br>2210-B Larch Street, Fairview<br>4821 USA
  </div>
  <div class="body-text">
    <p>Thank you for choosing our practice for your family's dental care. We are pleased to confirm your upcoming visit and look forward to meeting you. Our team offers gentle cleanings, exams, whitening and restorative treatment in a calm, welcoming office near the foothills. Please arrive ten minutes early to complete any paperwork and bring your insurance card and a list of current medications.</p>
    <p>If you need to change your appointment, please call our front desk at least one day in advance so we can offer the time to another patient.</p>
    <p>We are happy to answer any questions before your visit.</p>
    <p>Our office also provides cosmetic consultations, clear aligners and same day emergency care for existing patients. Parking is available directly in front of the building, and the entrance is fully accessible. Children are always welcome, and we schedule family visits back to back whenever possible.</p>
    <p>Thank you again for your trust. We look forward to caring for your smile for many years to come, and we are always glad to welcome new friends and neighbors into our practice.</p>
    <p>With warm regards from all of us at the office.</p>
  </div>
  <div class="signature">
    <div class="script">owen pratt</div>
    <div class="name">Owen Pratt</div>
    <div class="role">Managing Director</div>
  </div>
  <div class="footer">
    <div class="addr">5120 Ridgecrest Road, Granite Bay, CA 95790</div>
    <div><span class="label">Phone:</span> 530-555-0142 | <span class="label">Fax:</span> 530-555-0187 | <span class="label">Email:</span> mjosgood@mail.com | <span class="label">Web:</span> www.hollowmeredentalcare.com</div>
  </div>
</section>

<section class="sheet envelope-front">
  <div class="brand"><span class="dot"></span><span>Hollowmere Dentalcare</span></div>
  <div class="return-address">5120 Ridgecrest Road<br>Granite Bay, CA 95790</div>
  <svg class="wave" style="top:0;height:237px" viewBox="0 0 548 237" preserveAspectRatio="none">
    <path d="M0 200 C150 188 330 228 548 198 L548 237 L0 237Z" fill="var(--blue)"/>
    <path d="M0 190 C70 178 150 184 185 196 C120 190 50 193 0 202Z" fill="var(--green)"/>
    <path d="M370 216 C450 214 510 204 548 190 L548 197 C500 210 440 218 370 216Z" fill="var(--green)"/>
  </svg>
</section>

<section class="sheet envelope-back">
  <svg class="wave" style="top:0;height:72px" viewBox="0 0 551 72" preserveAspectRatio="none">
    <path d="M2 0 C10 30 14 62 40 65 L515 66 C535 64 545 30 551 0" fill="none" stroke="#ccc" stroke-width="2"/>
  </svg>
  <div class="brand"><span class="dot"></span><span>Hollowmere Dentalcare</span></div>
  <div class="site">www.hollowmeredentalcare.com</div>
</section>

</body>
</html>
```